Redesign of the UI of a customer service platform

To improve the user experience of our customers, we need a new design for our agent interface of our customer service platform (lunorbit.com).
The focus will be on the dashboard and the inbox screens (see attached) along with the common UI elements (Buttons, menu, fonts, forms...)
We want a simple and distinctive design

Target Market(s)

Worldwide

Industry/Entity Type

It Service

Number of Pages Required

3 page

Font styles to use
Sans Serif

Requirements
Must have
• New Onboarding page: this is a new page that is shown to user the first time they login to the platform. This will replace the current onboarding screen (setup SMS, Setup widget...etc)
• Dashboard page: to access important information and activate services (see screenshot from current site)
• Inbox page: to manage all the interactions with customers. (see screenshot from current site)
• UI elements (buttons, menus, forms, tables, fonts, color palette)

```html
<!DOCTYPE html>
<html lang="en">
<head>
<meta charset="utf-8">
<title>Lunorbit — Dashboard</title>
<link href="https://fonts.googleapis.com/css2?family=Roboto:wght@300;400;500&display=swap" rel="stylesheet">
<style>
:root{
  --teal:#1fbfad;
  --side:#3b3b3b;
  --side-line:#2f2f2f;
  --ink:#333;
  --muted:#8a8a8a;
  --line:#e2e2e2;
  --panel:#f9f9f9;
  --bg:#fff;
  --red:#f04a24;
  --green:#4cd964;
  --orange:#f79577;
}
*{box-sizing:border-box;margin:0;padding:0}
html,body{width:1200px;height:796px;overflow:hidden;background:var(--bg);font-family:"Roboto",sans-serif;color:var(--ink)}
.app{position:relative;width:1200px;height:796px}
.sidebar{position:absolute;left:0;top:0;width:181px;height:796px;background:var(--side)}
.brand{height:64px;background:var(--teal);display:flex;align-items:center;padding:0 16px;color:#fff;justify-content:space-between}
.brand-name{font-size:18px;font-weight:500;display:flex;align-items:center;gap:6px}
.brand-dot{width:14px;height:14px;border-radius:50%;background:#fff}
.nav-item{height:71px;display:flex;align-items:center;gap:16px;padding-left:19px;color:#fff;font-size:13.5px;border-bottom:1px solid var(--side-line)}
.nav-item svg{width:26px;height:26px;fill:#fff}
.nav-item.active{background:var(--teal);position:relative}
.nav-item.active::after{content:"";position:absolute;right:-7px;top:28px;border:7px solid transparent;border-left-color:var(--teal);border-right:0}
.topbar{position:absolute;left:181px;top:0;right:0;height:46px;background:#f5f5f5;display:flex;align-items:center;padding-left:23px;font-size:17px}
.top-icons{position:absolute;right:20px;top:12px;display:flex;gap:26px}
.top-icons svg{width:22px;height:22px;fill:#333}
.badge{position:absolute;background:var(--red);color:#fff;font-size:9px;width:14px;height:14px;border-radius:50%;display:flex;align-items:center;justify-content:center}
.stats{position:absolute;left:196px;top:60px;width:183px;border:1px solid var(--line)}
.stat{height:109px;position:relative;border-bottom:1px solid var(--line);text-align:center;padding:17px 0 0 28px}
.stat:last-child{border-bottom:0}
.stat-corner{position:absolute;left:0;top:0;width:70px;height:70px;background:var(--teal);clip-path:polygon(0 0,100% 0,0 100%)}
.stat-corner svg{position:absolute;left:11px;top:9px;width:20px;height:20px;fill:#fff}
.stat-val{font-size:24px;font-weight:300}
.stat-txt{font-size:11px;color:var(--muted);line-height:18px;margin-top:8px;font-weight:300}
.reports{position:absolute;left:404px;top:62px;width:796px;height:380px;background:var(--panel);border:1px solid #eee}
.panel-head{height:46px;border-bottom:1px solid #eaeaea;display:flex;align-items:center;padding:0 18px;justify-content:space-between}
.tabs{display:flex;gap:14px}
.tabs svg{width:15px;height:15px;fill:#999}
.tabs svg.on{fill:var(--teal)}
.panel-title{font-size:17px}
.rep-title{position:absolute;left:15px;top:64px;font-size:13px}
.rep-sub{position:absolute;left:15px;top:86px;font-size:11px;color:var(--muted)}
.toggle{position:absolute;right:20px;top:69px;display:flex;border:1px solid #ddd}
.toggle span{width:37px;height:25px;background:#fff}
.toggle span:first-child{background:#e6e6e6;border-right:1px solid #ddd}
.media{position:absolute;left:18px;top:111px;width:758px;height:245px;background:linear-gradient(135deg,#c9c4c0,#e9e9ee 45%,#8d95a8);}
.play{position:absolute;left:365px;top:100px;width:60px;height:60px;border-radius:50%;border:2px solid #fff;background:rgba(0,0,0,.55)}
.play::after{content:"";position:absolute;left:24px;top:17px;border:12px solid transparent;border-left:18px solid #fff;border-right:0}
.progress{position:absolute;left:33px;right:50px;top:223px;height:2px;background:#fff}
.progress i{position:absolute;left:0;top:0;width:29%;height:2px;background:var(--teal)}
.progress b{position:absolute;left:29%;top:-4px;width:10px;height:10px;border-radius:50%;background:#fff}
.plan{position:absolute;left:404px;top:466px;width:796px;height:284px;background:var(--panel);border:1px solid #eee}
.btn{background:#a9a9a9;color:#fff;font-size:11px;padding:7px 14px;border:0}
.plan-list{position:absolute;left:0;top:45px;width:147px;border-right:1px solid var(--line);height:238px}
.plan-row{height:80px;border-bottom:1px solid var(--line);display:flex;align-items:center;padding-left:10px;gap:12px;position:relative}
.plan-row:last-child{border-bottom:0}
.plan-row svg{width:24px;height:24px;fill:#333}
.plan-row .badge{right:8px;top:5px;width:18px;height:18px;font-size:11px}
.pn{font-size:14px;color:#555}
.pu{font-size:12px;color:var(--muted);margin-top:3px;padding-left:3px}
.addon{position:absolute;left:168px;width:610px;border-left:2px solid #eaeaea;padding-left:14px}
.addon.first{border-left-color:var(--orange)}
.addon h4{font-size:13px;font-weight:400;margin-bottom:8px}
.addon p{font-size:11px;color:var(--muted);line-height:16px;width:300px;padding-left:2px}
.tag{position:absolute;right:0;top:22px;background:var(--green);color:#fff;font-size:9px;padding:4px 11px}
</style>
</head>
<body>
<div class="app">
  <aside class="sidebar">
    <div class="brand"><span class="brand-name"><span class="brand-dot"></span>lunorbit</span>
      <svg width="20" height="14" viewBox="0 0 20 14"><rect width="20" height="2" fill="#333"/><rect y="6" width="20" height="2" fill="#333"/><rect y="12" width="20" height="2" fill="#333"/></svg></div>
    <div class="nav-item active"><svg viewBox="0 0 24 24"><path d="M12 5a10 10 0 0 0-10 10v3h20v-3A10 10 0 0 0 12 5zm0 2.5a7.5 7.5 0 0 1 7.5 7.5v.5h-15V15A7.5 7.5 0 0 1 12 7.5zm3.5 2L12 13a1.5 1.5 0 1 0 1 1z"/></svg>Dashboard</div>
    <div class="nav-item"><svg viewBox="0 0 24 24"><path d="M2 12h6l2 3h4l2-3h6v8H2zM11 3h2v6h3l-4 4-4-4h3z"/></svg>Inbox</div>
    <div class="nav-item"><svg viewBox="0 0 24 24"><path d="M14 2l8 8-12 12-8-8zm0 3L5 14l5 5 9-9z"/></svg>Tickets</div>
    <div class="nav-item"><svg viewBox="0 0 24 24"><circle cx="12" cy="8" r="3.5"/><circle cx="5" cy="9" r="2.5"/><circle cx="19" cy="9" r="2.5"/><path d="M5 20v-3a7 7 0 0 1 14 0v3zM0 18v-2a4 4 0 0 1 5-3.5 8 8 0 0 0-2 5.5zm24 0v-2a4 4 0 0 0-5-3.5 8 8 0 0 1 2 5.5z"/></svg>Clients</div>
    <div class="nav-item"><svg viewBox="0 0 24 24"><path d="M2 22h20v-2H2zM3 18h3v-3H3zm5 0h3v-6H8zm5 0h3v-8h-3zm5 0h3V8h-3zM3 12l6-5 4 3 7-7 1 1-8 8-4-3-5 4z"/></svg>Reports</div>
    <div class="nav-item"><svg viewBox="0 0 24 24"><path d="M10 1h4l.6 3 2.4 1.2 2.6-1.7 2.9 2.9-1.7 2.6L22 10v4l-3 .6-1.2 2.4 1.7 2.6-2.9 2.9-2.6-1.7L13.8 20 14 23h-4l-.6-3-2.4-1.2-2.6 1.7-2.9-2.9 1.7-2.6L2 14v-4l3-.6L6.2 7 4.5 4.4l2.9-2.9L10 3.2zm2 7a4 4 0 1 0 0 8 4 4 0 0 0 0-8z"/></svg>Settings</div>
  </aside>

  <header class="topbar">Dashboard
    <div class="top-icons">
      <svg viewBox="0 0 24 24"><path d="M2 12h6l2 3h4l2-3h6v8H2zM11 5h2v4h3l-4 4-4-4h3z"/></svg>
      <svg viewBox="0 0 24 24"><path d="M14 2l8 8-12 12-8-8zm0 3L5 14l5 5 9-9z"/></svg>
    </div>
    <span class="badge" style="right:70px;top:8px">1</span>
  </header>

  <section class="stats">
    <div class="stat"><div class="stat-corner"><svg viewBox="0 0 24 24"><circle cx="12" cy="7" r="5"/><path d="M4 23v-5a5 5 0 0 1 5-5h6a5 5 0 0 1 5 5v5z"/></svg></div><div class="stat-val">0/0</div><div class="stat-txt">Lorem Ipsum is simply<br>dummy text</div></div>
    <div class="stat"><div class="stat-corner"><svg viewBox="0 0 24 24"><path d="M14 2l8 8-12 12-8-8zm0 3L5 14l5 5 9-9z"/></svg></div><div class="stat-val">0/0</div><div class="stat-txt">Lorem Ipsum is simply<br>dummy text</div></div>
    <div class="stat"><div class="stat-corner"><svg viewBox="0 0 24 24"><path d="M9 3c5 0 8 3 8 6s-3 6-8 6l-5 3 1-4C3 13 1 11 1 9c0-3 3-6 8-6zm10 8c3 1 4 3 4 5 0 1-1 3-2 4l1 3-4-2c-3 0-5-1-6-3 4-1 7-4 7-7z"/></svg></div><div class="stat-val">0/0</div><div class="stat-txt">Lorem Ipsum is simply<br>dummy text</div></div>
    <div class="stat"><div class="stat-corner"><svg viewBox="0 0 24 24"><path d="M4 2h10v20H4zm2 3v12h6V5zm10 2h6v6h-3l-3 3z"/></svg></div><div class="stat-val">0/0</div><div class="stat-txt">Lorem Ipsum is simply<br>dummy text</div></div>
  </section>

  <section class="reports">
    <div class="panel-head">
      <div class="tabs">
        <svg viewBox="0 0 24 24"><path d="M4 2h10v20H4zm2 3v12h6V5zm10 2h6v6h-3l-3 3z"/></svg>
        <svg viewBox="0 0 24 24"><path d="M9 3c5 0 8 3 8 6s-3 6-8 6l-5 3 1-4C3 13 1 11 1 9c0-3 3-6 8-6zm10 8c3 1 4 3 4 5 0 1-1 3-2 4l1 3-4-2c-3 0-5-1-6-3 4-1 7-4 7-7z"/></svg>
        <svg viewBox="0 0 24 24"><path d="M14 2l8 8-12 12-8-8zm0 3L5 14l5 5 9-9z"/></svg>
        <svg class="on" viewBox="0 0 24 24"><circle cx="12" cy="7" r="5"/><path d="M4 23v-5a5 5 0 0 1 5-5h6a5 5 0 0 1 5 5v5z"/></svg>
      </div>
      <span class="panel-title">Reports</span>
    </div>
    <div class="rep-title">Lorem Ipsum is simply dummy text</div>
    <div class="rep-sub">Lorem Ipsum is simply dummy text</div>
    <div class="toggle"><span></span><span></span></div>
    <div class="media" role="img" aria-label="Video still: hands reviewing printed bar charts with a pen">
      <div class="play"></div>
      <div class="progress"><i></i><b></b></div>
    </div>
  </section>

  <section class="plan">
    <div class="panel-head"><button class="btn">Upgrade</button><span class="panel-title">Plan &amp; Add-ons</span></div>
    <div class="plan-list">
      <div class="plan-row"><svg viewBox="0 0 24 24"><circle cx="12" cy="8" r="3.5"/><circle cx="5" cy="9" r="2.5"/><circle cx="19" cy="9" r="2.5"/><path d="M5 20v-3a7 7 0 0 1 14 0v3z"/></svg><div><div class="pn">Lorem Ipsum</div><div class="pu">Unlimited</div></div><span class="badge">1</span></div>
      <div class="plan-row"><svg viewBox="0 0 24 24"><path d="M2 22h20v-2H2zM3 18h3v-3H3zm5 0h3v-6H8zm5 0h3v-8h-3zm5 0h3V8h-3zM3 12l6-5 4 3 7-7 1 1-8 8-4-3-5 4z"/></svg><div><div class="pn">Lorem Ipsum</div><div class="pu">Unlimited</div></div><span class="badge">1</span></div>
      <div class="plan-row"><svg viewBox="0 0 24 24"><path d="M2 12h6l2 3h4l2-3h6v8H2zM11 3h2v6h3l-4 4-4-4h3z"/></svg><div><div class="pn">Lorem Ipsum</div><div class="pu">Unlimited</div></div><span class="badge">1</span></div>
    </div>
    <div class="addon first" style="top:64px"><h4>Lorum Ipsum</h4><p>Pellentesque habitant morbi tristique senectus et netus et malesuada fames ac turpis egestas. morbi...</p><span class="tag">✓ Activted</span></div>
    <div class="addon" style="top:135px"><h4>Lorum Ipsum</h4><p>Pellentesque habitant morbi tristique senectus et netus et malesuada fames ac turpis egestas. morbi...</p><span class="tag">✓ Activted</span></div>
    <div class="addon" style="top:205px"><h4>Lorum Ipsum</h4><p>Pellentesque habitant morbi tristique senectus et netus et malesuada fames ac turpis egestas. morbi...</p><span class="tag">✓ Activted</span></div>
  </section>
</div>
</body>
</html>
```